We need our current web site completely overhauled logo and all. www.maplecrestkidsclub.com

This is a web site for a before and after school program for kids. I would like to see a fresh and cleaner version. The current version was created 8 to 10 years ago.
www.maplecrestkidsclub.com

```html
<!DOCTYPE html>
<html lang="en">
<head>
<meta charset="utf-8">
<title>Maplecrest Kids Club</title>
<link href="https://fonts.googleapis.com/css2?family=Source+Sans+3:wght@300;400;600&display=swap" rel="stylesheet">
<style>
:root{
  --green-dark:#0a3f1f;
  --green:#0e6a37;
  --green-brand:#145c2c;
  --orange:#f39418;
  --orange-dark:#e57a05;
  --leaf:#6aa124;
  --teal:#1ca4c6;
  --pink:#ea4f9c;
  --text:#5a5a5a;
  --heading:#333;
  --footer:#efefef;
  --white:#fff;
}
*{margin:0;padding:0;box-sizing:border-box}
html,body{width:1104px;height:1200px;overflow:hidden}
body{font-family:"Source Sans 3",sans-serif;background:var(--white);position:relative;color:var(--text)}
.scenery{position:absolute;left:0;top:0;width:1104px;height:503px;
  background:
   radial-gradient(ellipse 160px 260px at 1080px 330px,#8bc84a 0%,rgba(139,200,74,.6) 45%,rgba(255,255,255,0) 75%),
   radial-gradient(ellipse 200px 160px at 20px 360px,#9fd25a 0%,rgba(159,210,90,.5) 50%,rgba(255,255,255,0) 80%),
   linear-gradient(180deg,#cfe9f4 0%,#eaf6fb 45%,#ffffff 100%);}
.logo{position:absolute;left:107px;top:38px;display:flex;align-items:center;gap:10px}
.logo-dot{width:30px;height:30px;border-radius:50%;background:var(--green-brand)}
.logo-name{font-weight:600;font-size:27px;line-height:28px;color:var(--green-brand);width:150px}
.top-links{position:absolute;right:115px;top:12px;font-size:14px;color:#333;display:flex;gap:6px}
.top-links .sep{color:#555}
.social{position:absolute;left:869px;top:85px;display:flex;gap:8px}
.social span{width:24px;height:24px;border-radius:3px;background:var(--green)}
.main-nav{position:absolute;left:105px;top:125px;width:894px;height:45px;display:flex;
  background:linear-gradient(180deg,#0f7440 0%,#0a5129 55%,#073d1e 100%);border-radius:4px 4px 0 0}
.main-nav a{color:var(--white);text-decoration:none;font-size:16px;display:flex;align-items:center;justify-content:center;border-right:1px solid rgba(255,255,255,.18)}
.main-nav a:last-child{border-right:none}
.hero{position:absolute;left:105px;top:170px;width:894px;height:333px;
  background:linear-gradient(100deg,#b87b5a 0%,#e0b79a 25%,#c98a4a 45%,#d8b893 65%,#c7a276 85%,#e2a22a 100%);border-radius:0 0 4px 4px}
.hero-dots{position:absolute;left:513px;top:479px;display:flex;gap:3px}
.hero-dots span{width:14px;height:14px;border-radius:50%;background:var(--white);box-shadow:0 0 2px rgba(0,0,0,.3)}
.hero-dots span.active{background:#f06a1a}
.intro{position:absolute;left:0;top:538px;width:1104px;text-align:center}
.intro h1{font-weight:400;font-size:32px;color:var(--heading)}
.intro p{font-weight:300;font-size:12.6px;line-height:19.3px;width:800px;margin:10px auto 0;color:#666}
.btn-main{display:inline-block;margin-top:15px;width:108px;height:32px;line-height:32px;border-radius:3px;
  background:linear-gradient(180deg,#ffa62a,var(--orange-dark));color:var(--white);font-size:14px;text-decoration:none}
.cards{position:absolute;left:118px;top:729px;display:flex;gap:13px}
.card{width:210px;height:251px;border:1px solid #e3e3e3;border-radius:3px;padding:10px;box-shadow:0 3px 6px rgba(0,0,0,.05)}
.card-photo{height:113px}
.card h2{font-weight:600;font-size:16px;margin:10px 0 4px 2px}
.card p{font-size:11.2px;line-height:17.5px;color:#555;margin-left:2px}
.card .btn{display:inline-block;margin:8px 0 0 2px;width:76px;height:22px;line-height:22px;text-align:center;color:var(--white);font-size:10px;border-radius:2px;text-decoration:none}
.email h2{color:var(--leaf)} .email .btn{background:var(--leaf)}
.health h2{color:var(--orange-dark)} .health .btn{background:var(--orange-dark)}
.tuition h2{color:var(--teal)} .tuition .btn{background:var(--teal)}
.kids h2{color:var(--pink)} .kids .btn{background:var(--pink)}
.footer{position:absolute;left:0;top:1078px;width:1104px;height:122px;background:var(--footer)}
.footer-links{position:absolute;left:114px;top:30px;font-size:13.5px;color:#333;display:flex;gap:6px}
.copyright{position:absolute;left:114px;top:58px;font-size:11px;color:#888;font-weight:300}
</style>
</head>
<body>
<div class="scenery" role="img" aria-label="Painted sky with soft clouds, green hills and tulips"></div>

<div class="logo"><span class="logo-dot"></span><span class="logo-name">Maplecrest Kids Club</span></div>

<nav class="top-links"><span>Home</span><span class="sep">|</span><span>Locations</span><span class="sep">|</span><span>Careers</span><span class="sep">|</span><span>Events</span><span class="sep">|</span><span>Contact</span></nav>

<div class="social" aria-label="Social links"><span></span><span></span><span></span><span></span></div>

<nav class="main-nav">
  <a style="width:119px">PROGRAM</a>
  <a style="width:136px">MAPLECREST</a>
  <a style="width:154px">TUITION PORTAL</a>
  <a style="width:148px">PARTY &amp; RENTALS</a>
  <a style="width:107px">KIDS PLACE</a>
  <a style="width:102px">ABOUT US</a>
  <a style="width:128px">MONTESSORI</a>
</nav>

<div class="hero" role="img" aria-label="Photo of a smiling family with children holding gifts"></div>
<div class="hero-dots"><span class="active"></span><span></span><span></span><span></span><span></span></div>

<section class="intro">
  <h1>In Case You Do Not Know Us</h1>
  <p>The Maplecrest Kids Club Before and After School Program exists to provide programming of the highest quality for your children, stressing a safe, secure environment; a nurturing, professional staff and lots of fun. We are committed to providing a fun-filled, rewarding program that supports the physical, mental, emotional and spiritual development of school-age children and their families to the fullest potential in order to improve their quality of life.</p>
  <a class="btn-main">LEARN MORE</a>
</section>

<div class="cards">
  <article class="card email">
    <div class="card-photo" role="img" aria-label="Photo of a hand touching a world map of connected mail icons" style="background:linear-gradient(135deg,#e8e8e8,#c9c9c9)"></div>
    <h2>EMAIL SYSTEM</h2>
    <p>Mauris vel lacus vitae felis vestibulum volutpat. Etiam est nunc, venenatis in, tristique eu, imperdiet ac, nisl.</p>
    <a class="btn">READ MORE</a>
  </article>
  <article class="card health">
    <div class="card-photo" role="img" aria-label="Photo of children eating apples" style="background:linear-gradient(135deg,#c98a5a,#e39a3c 60%,#f0c9a0)"></div>
    <h2>HEALTH TIPS</h2>
    <p>Mauris vel lacus vitae felis vestibulum volutpat. Etiam est nunc, venenatis in, tristique eu, imperdiet ac, nisl.</p>
    <a class="btn">READ MORE</a>
  </article>
  <article class="card tuition">
    <div class="card-photo" role="img" aria-label="Photo of a teacher with students in a library" style="background:linear-gradient(135deg,#5fb2d6,#c9a07c 55%,#8a6a4e)"></div>
    <h2>TUITION PORTAL</h2>
    <p>Mauris vel lacus vitae felis vestibulum volutpat. Etiam est nunc, venenatis in, tristique eu, imperdiet ac, nisl.</p>
    <a class="btn">READ MORE</a>
  </article>
  <article class="card kids">
    <div class="card-photo" role="img" aria-label="Photo of children running in a park" style="background:linear-gradient(135deg,#7fb24a,#b9d98a 55%,#5e8f3a)"></div>
    <h2>KID’S PLACE</h2>
    <p>Mauris vel lacus vitae felis vestibulum volutpat. Etiam est nunc, venenatis in, tristique eu, imperdiet ac, nisl.</p>
    <a class="btn">READ MORE</a>
  </article>
</div>

<footer class="footer">
  <nav class="footer-links"><span>HOME</span>|<span>ABOUT</span>|<span>PROGRAM</span>|<span>MAPLECREST</span>|<span>TUITION PORTAL</span>|<span>PARTY &amp; RENTALS</span>|<span>KIDS PLACE</span>|<span>ABOUT US</span>|<span>MONTESSORI</span>|<span>CONTACT</span></nav>
  <p class="copyright">© 2013 Company Name. All right reserved. &nbsp;Term of Use</p>
</footer>
</body>
</html>
```